verdant manor grounds simple classy business card design

my name is owen brackley and I run a gardening business aimed at high class verdant manor grounds. the business name is verdant manor grounds and our logo was designed on brief hive .My clientel are anything from residential homes to businesses. I take pride in my work and know that I offer a service like no other in my area.
The business card will be used to represent my business and I want it to be not only rememberable, but simplistic and modern. Eye catching too. Of course I would like it relatable to gardening and appealing to the correct clientel - those being garden enthusiasts, prestigious homes and businesses that are after top of the line gardening services like no other on the market.
I am not a typical lawn mowing business so I don't want a typical card design that represents that. The gardens I work with are generally million dollar properties with owners who are very garden proud looking for upkeep and guidance from me along with sometimes whole new garden designs. I want the business cards to show to my clients that I take pride, as they do, in their garden. And I want them to know from my card that I am a professional, qualified horticulturist offering them a top of the line service for life. I want them to refer my business on. I want them to look at my business card and see class and professionalism in a modern unique bold way.
The card should be simple with the possibility of the logo on the front being embossed/debossed and my details on the back the card should have a organic garden feel it's very important to me that it is absolutely perfect
I am also very open to ideas and suggestions so look forward to seeing the designs. the business logo has been supplied with this project and I want the card to be double sided

Contact info is
Owen Brackley - Managing Director / Horticulturist
Phone : 0481 562 907
Email: owenbrackley@verdantmanorgrounds.example.au

Target Market(s)

high class gardens residential and commercial

Industry/Entity Type

Gardener

Contact Information for Business Card

Contact info is
Phone : 0481 562 907

PLEASE MAKE CARD DOUBLE SIDED

Requirements
Must have
• organic simple classy modern feel
• must flow with the current logo that has been supplied with this project
• Double sided
• Must explain in a simple way that I deal with high end gardens and I'm a qualified horticulturist
Nice to have
• embossed debossed logo
Should not have
• shouldn't be to busy or cheap looking

```html
<!DOCTYPE html>
<html lang="en">
<head>
<meta charset="UTF-8">
<title>Verdant Manor Grounds – Business Card</title>
<link href="https://fonts.googleapis.com/css2?family=Lato:wght@300;400&family=Oswald:wght@600&display=swap" rel="stylesheet">
<style>
  :root {
    --backdrop: #1f2a3d;
    --card-dark: #3a3a36;
    --card-dark-edge: #2c2c29;
    --gold: #c9a85c;
    --gold-light: #e3cf95;
    --gold-deep: #a8863f;
    --logo-ink: #2f2f2b;
  }
  * { box-sizing: border-box; margin: 0; padding: 0; }
  html, body { width: 1200px; height: 800px; overflow: hidden; }
  body {
    background: var(--backdrop);
    font-family: "Lato", sans-serif;
    position: relative;
  }
  .card {
    position: absolute;
    top: 100px;
    width: 360px;
    height: 600px;
    border-radius: 4px;
    overflow: hidden;
    box-shadow: 0 18px 40px rgba(0,0,0,0.45);
  }

  /* Back side: details */
  .card--details {
    left: 190px;
    background: linear-gradient(160deg, var(--card-dark-edge) 0%, var(--card-dark) 45%, var(--card-dark-edge) 100%);
    color: var(--gold);
  }
  .wordmark {
    display: flex;
    align-items: center;
    gap: 10px;
    color: var(--gold);
    font-family: "Lato", sans-serif;
    font-weight: 400;
    letter-spacing: 0.18em;
    text-transform: uppercase;
    font-size: 15px;
    line-height: 1.35;
    white-space: nowrap;
  }
  .wordmark__dot {
    width: 34px; height: 34px;
    border-radius: 50%;
    background: currentColor;
    flex: none;
  }
  .card--details .wordmark { position: absolute; top: 56px; left: 40px; }

  .person { position: absolute; top: 240px; left: 84px; }
  .person__name {
    font-family: "Oswald", sans-serif;
    font-weight: 600;
    font-size: 30px;
    letter-spacing: 0.01em;
    text-transform: uppercase;
    line-height: 1;
    white-space: nowrap;
  }
  .person__role {
    font-weight: 300;
    font-size: 17px;
    line-height: 1.2;
    margin-top: 6px;
  }
  .contacts {
    position: absolute; top: 362px; left: 40px; right: 16px;
    list-style: none;
    font-weight: 300;
    font-size: 12px;
    white-space: nowrap;
  }
  .contacts li { display: flex; align-items: center; gap: 12px; margin-bottom: 9px; }
  .contacts__bullet { width: 12px; height: 12px; background: var(--gold); flex: none; }
  .company {
    position: absolute; top: 474px; left: 40px;
    font-weight: 400;
    font-size: 17px;
    text-transform: uppercase;
    line-height: 1.5;
    white-space: nowrap;
  }

  /* Front side: gold panel with wordmark */
  .card--front {
    left: 650px;
    background: var(--card-dark);
  }
  .gold-panel {
    position: absolute;
    top: 100px; bottom: 100px; left: 0; right: 0;
    background:
      radial-gradient(ellipse at 35% 30%, var(--gold-light) 0%, transparent 60%),
      linear-gradient(150deg, var(--gold-light) 0%, var(--gold) 45%, var(--gold-deep) 100%);
  }
  .card--front .wordmark {
    position: absolute;
    top: 150px; left: 50%;
    transform: translateX(-50%);
    flex-direction: column;
    text-align: center;
    color: var(--logo-ink);
  }
</style>
</head>
<body>

  <section class="card card--details" aria-label="Business card back with contact details">
    <div class="wordmark">
      <span class="wordmark__dot"></span>
      <span>Verdant Manor<br>Grounds</span>
    </div>

    <div class="person">
      <h1 class="person__name">Owen Brackley</h1>
      <p class="person__role">Managing Director /<br>Horticulturist</p>
    </div>

    <ul class="contacts">
      <li><span class="contacts__bullet"></span>0481 562 907</li>
      <li><span class="contacts__bullet"></span>www.verdantmanorgrounds.example</li>
      <li><span class="contacts__bullet"></span>owenbrackley@verdantmanorgrounds.example.au</li>
    </ul>

    <p class="company">Larchfield Holdings Ltd<br>Supply Address</p>
  </section>

  <section class="card card--front" aria-label="Business card front with gold panel">
    <div class="gold-panel">
      <div class="wordmark">
        <span class="wordmark__dot"></span>
        <span>Verdant Manor<br>Grounds</span>
      </div>
    </div>
  </section>

</body>
</html>
```